Real Estate Website - Phase I

We are looking to re-design our company website completely.
This will be for a real estate company which focuses on multiple lines of business/customers, including

1) Buyers - Investors, Owner Occupants
2) Sellers - Short Sales, Limited Services/Flat Fee, and Corporate/REO clients (the last being our core current customer)
3) Other Services: Default Services, Institutional Property Management, Field and Inspection Services
4) Agent FAQ's, instructions, etc to tie into our web-based offer management systems

For a brief understanding of what we do - Please see www.plavetrix.com. Current site does not address all of our current services.

Website must be able to be edited/added onto over time. We are also looking at redirects so that certain pages/sections can be given unique domain names to drive core customers to.

We work both with normal agents and buyers and large scale financial institutions, therefore our focus must be specific to each unique group based on the applicable page(s).

We had an incorrect amount in this brief.  It has since been corrected.

Please re-review.

Industry/Entity Type

Real Estate

Requirements
Must have
• *Property Search/Display - By various criteria AND by map
*Property Management back end for putting in new properties
*MObile Version or Mobile Friendly
*Analytics
*Contact Management and Lead Capture functions, including ability to export or use from site for email marketing campaigns. Lead capture must be able to sort by various criteria to tailor campaigns, ability to send out auto notices to staff and those signing up, etc.
* Signup option w/ functions for viewing not yet on market properties (subscription). This needs to be able to let buyers set search criteria and be auto notified whenever a property was listed or adjusted that met their criteria.
* SEO Optimization
* Syndication options to allow ease of syndication
* FAQ's and assistance pages to agents working with us
* Blog, social media boxes
* Ability for buyers to submit initial offers direct
* Functions and pages specific to below, with ability to cross promote and track (inquiry forms, etc to the below)
*Dedicated or preferred lender(s)
* Preferred vendors, etc

```html
<!DOCTYPE html>
<html lang="en">
<head>
<meta charset="utf-8">
<title>Tidewater Homes – 1820 Palm Crest Dr</title>
<link href="https://fonts.googleapis.com/css2?family=Noto+Serif:wght@400;700&family=Arimo:wght@400;700&display=swap" rel="stylesheet">
<style>
:root{
  --page:#ebebea;
  --header:#f4f3f1;
  --panel:#ffffff;
  --nav:#3b3b3b;
  --coral:#e46e5c;
  --blue:#1f5fa9;
  --blue-dark:#154c8c;
  --link:#2a62b0;
  --orange:#e58a50;
  --yellow:#f0b428;
  --text:#555555;
  --muted:#777777;
  --ink:#333333;
  --chip:#f0f0f0;
  --icon:#8a8a8a;
}
*{box-sizing:border-box;margin:0;padding:0}
html,body{width:1200px;height:794px;overflow:hidden;background:var(--page)}
body{font-family:"Arimo",Arial,sans-serif;color:var(--text);position:relative}
.serif{font-family:"Noto Serif",Georgia,serif}
.abs{position:absolute}

.site-header{position:absolute;left:0;top:0;width:1200px;height:170px;background:var(--header);border-bottom:1px solid #dedede}
.brand{left:186px;top:34px;display:flex;align-items:center;gap:12px}
.brand-mark{width:48px;height:48px;border-radius:50%;background:var(--coral)}
.brand-name{font-family:"Noto Serif",Georgia,serif;color:var(--coral);font-size:30px;line-height:1;letter-spacing:1px}

.login{left:732px;top:32px;width:251px;height:19px;display:flex;border:1px solid #d0d0d0;background:#fff;font-size:7px}
.login span{display:flex;align-items:center;padding-left:7px;color:#555}
.login .email{width:115px;border-right:1px solid #ddd}
.login .pass{width:78px;letter-spacing:1px;font-size:8px}
.login .btn{flex:1;background:#13264a;color:#fff;font-weight:700;font-size:8px;padding-left:9px}
.social{left:732px;top:62px;display:flex;align-items:center;gap:4px}
.like{height:16px;padding:0 5px;border:1px solid #c9c9c9;background:#eef0f5;font-size:8px;color:#3b5998;display:flex;align-items:center}
.count{height:16px;padding:0 3px;border:1px solid #c9c9c9;background:#fff;font-size:8px;display:flex;align-items:center}
.social-icons{left:805px;top:62px;display:flex;gap:5px}
.social-icons i{width:18px;height:18px;background:#9a9a9a;border-radius:2px;display:block}

.main-nav{left:188px;top:108px;width:801px;height:50px;background:linear-gradient(#454545,#333);box-shadow:0 1px 3px rgba(0,0,0,.3);display:flex}
.main-nav a{color:#fff;text-decoration:none;font-size:14px;display:flex;align-items:center;padding:0 17px;border-right:1px solid #2a2a2a}
.main-nav a.current{background:var(--coral);padding:0 18px}
.nav-search{left:793px;top:121px;width:179px;height:21px;background:#f1f1f1;border-radius:3px;font-size:12px;color:#777;display:flex;align-items:center;padding-left:9px}
.nav-search b{position:absolute;right:0;top:0;width:33px;height:21px;background:var(--yellow);border-radius:0 3px 3px 0}

.card{position:absolute;background:var(--panel);border-radius:4px;box-shadow:0 1px 2px rgba(0,0,0,.08)}
.breadcrumb{left:187px;top:194px;width:535px;height:39px;font-size:10px;display:flex;align-items:center;padding-left:13px}
.breadcrumb strong{color:var(--ink);margin-right:12px}
.breadcrumb a{color:var(--link);text-decoration:none}
.print{position:absolute;right:13px;top:13px;width:16px;height:12px;border:2px solid #aaa;border-radius:2px}

.listing{left:187px;top:253px;width:533px;height:396px}
.photo{left:9px;top:8px;width:330px;height:244px;background:linear-gradient(#3a6fc4 0%,#8bb0e0 35%,#e8dcd6 55%,#c9bdb8 75%,#3a4a2c 100%)}
.title{left:348px;top:8px;width:180px;font-size:17px;line-height:21px;color:var(--blue);font-weight:400}
.date{left:348px;top:52px;font-size:10px;color:var(--muted);display:flex;align-items:center;gap:6px}
.date i{width:11px;height:11px;border:1px solid #aaa;display:block}
.features{left:348px;top:75px;display:grid;grid-template-columns:repeat(3,55px);grid-auto-rows:52px;gap:6px 5px}
.feature{background:var(--chip);border-radius:3px;display:flex;flex-direction:column;align-items:center;justify-content:flex-end;padding-bottom:5px;font-family:"Noto Serif",Georgia,serif;font-size:9.5px;color:var(--ink);gap:5px}
.feature svg{width:26px;height:22px;fill:var(--icon)}
.price-tag{left:356px;top:207px;width:163px;height:32px;background:var(--blue);color:#fff;text-align:right;padding:3px 8px 0 0;clip-path:polygon(0 0,100% 0,100% 100%,0 100%,12px 50%)}
.price-tag small{display:block;font-size:8px}
.price-tag strong{font-size:15px;font-weight:400}
.thumbs{left:9px;top:261px;display:grid;grid-template-columns:repeat(6,76px);grid-auto-rows:55px;gap:12px 11.8px}
.thumb{border:1px solid #ddd;padding:3px;background:#fff}
.thumb div{width:100%;height:100%}
.thumb.active{border-color:var(--blue)}

.description{left:187px;top:666px;width:535px;font-size:10px;line-height:16px;color:#666}
.description p{margin-bottom:15px}

.search-widget{left:741px;top:194px;width:245px;height:302px}
.widget-head{position:absolute;left:0;top:0;width:100%;height:35px;background:var(--nav);border-radius:4px 4px 0 0;color:#fff;font-family:"Noto Serif",Georgia,serif;font-size:15px;display:flex;align-items:center;padding-left:30px;gap:8px}
.widget-head svg{width:14px;height:14px}
.field{position:absolute;left:16px;font-size:10px;color:#666;line-height:12px}
.select{position:absolute;left:79px;width:139px;height:23px;border:1px solid #d3d3d3;border-radius:2px;background:linear-gradient(#fbfbfb,#ececec);font-size:9px;color:#666;padding:6px 10px;line-height:10px}
.select::after{content:"";position:absolute;right:0;top:0;width:24px;height:21px;border-left:1px solid #d3d3d3}
.select b{position:absolute;right:8px;top:9px;border:4px solid transparent;border-top:5px solid #555;z-index:1}
.range{position:absolute;left:16px;top:271px;font-size:10px;color:#666;line-height:12px}
.range strong{margin-left:15px;color:#555}
.slider{position:absolute;left:25px;width:202px;height:9px;border:1px solid #ccc;border-radius:5px;background:#fff}
.slider i{position:absolute;top:-3px;width:14px;height:13px;border:1px solid #bbb;border-radius:2px;background:#eee}
.widget-btn{position:absolute;left:152px;top:265px;width:65px;height:24px;background:linear-gradient(#2f7dd0,var(--blue-dark));border-radius:3px;color:#fff;font-size:11px;display:flex;align-items:center;justify-content:center}

.featured{left:741px;top:515px;width:245px;height:223px}
.featured h2,.recent{font-family:"Noto Serif",Georgia,serif;font-weight:400;font-size:16px;color:var(--blue)}
.featured h2{position:absolute;left:8px;top:6px}
.featured-photo{left:8px;top:37px;width:228px;height:114px;background:linear-gradient(#3c70c4 0%,#9bbbe4 40%,#e6dbd5 65%,#4a5a35 100%)}
.ribbon{left:124px;top:47px;width:112px;height:35px;background:var(--orange);color:#fff;text-align:right;padding:2px 8px 0 0;clip-path:polygon(0 0,100% 0,100% 100%,0 100%,10px 50%)}
.ribbon small{display:block;font-size:8px}
.ribbon strong{font-size:14px;font-weight:400}
.featured h3{position:absolute;left:8px;top:158px;font-family:"Noto Serif",Georgia,serif;font-weight:400;font-size:13px;color:var(--ink)}
.featured p{position:absolute;left:8px;top:184px;width:225px;font-size:10px;line-height:15px;color:#777}
.recent{position:absolute;left:748px;top:757px}
.recent-item{position:absolute;left:749px;top:784px;font-size:10px;color:#666}
</style>
</head>
<body>

<header class="site-header">
  <div class="abs brand"><span class="brand-mark"></span><span class="brand-name">TIDEWATER HOMES</span></div>
  <div class="abs login"><span class="email">Email Address</span><span class="pass">•••••••••••••</span><span class="btn">LOGIN</span></div>
  <div class="abs social"><span class="like">Like</span><span class="count">584</span></div>
  <div class="abs social-icons"><i></i><i></i><i></i><i></i><i></i><i></i><i></i><i></i></div>

  <nav class="abs main-nav">
    <a class="current" href="#">Home</a><a href="#">About</a><a href="#">Services</a><a href="#">Projects</a><a href="#">Blog</a><a href="#">Contacts</a>
  </nav>
  <div class="abs nav-search">Search<b></b></div>
</header>

<div class="card breadcrumb">
  <strong>You are here:</strong>
  <a href="#">Harborview Theme</a>&nbsp;/&nbsp;<a href="#">Single Family Home</a>&nbsp;/&nbsp;<a href="#">1820 Palm Crest Dr, Coral Fl 33150</a>
  <span class="print"></span>
</div>

<section class="card listing">
  <div class="abs photo" role="img" aria-label="Photo of a two-storey family house with a double garage"></div>
  <h1 class="abs title serif">1820 Palm Crest Dr, Coral Fl 33150</h1>
  <div class="abs date"><i></i>18 April, 2012</div>

  <div class="abs features">
    <div class="feature"><svg viewBox="0 0 26 22"><path d="M13 2 2 11h3v9h6v-6h4v6h6v-9h3z"/></svg>2500 Sq Ft</div>
    <div class="feature"><svg viewBox="0 0 26 22"><path d="M2 4h2v8h20v8h-2v-3H4v3H2zM6 8h5v4H6zM12 9h10v3H12z"/></svg>3 Beds</div>
    <div class="feature"><svg viewBox="0 0 26 22"><path d="M2 3h22v4h-2v13h-3V9H7v11H4V7H2zM8 11h10v2H8zM8 15h10v2H8z"/></svg>2 Garage</div>
    <div class="feature"><svg viewBox="0 0 26 22"><path d="M3 10h20v3a6 6 0 0 1-6 6H9a6 6 0 0 1-6-6zM5 10V4a2 2 0 0 1 4 0h-2v6z"/></svg>3 Baths</div>
    <div class="feature"><svg viewBox="0 0 26 22"><path d="M8 2h10l3 10H5zM12 12h2v6h4v2H8v-2h4z"/></svg>Unfurnish</div>
    <div class="feature"><svg viewBox="0 0 26 22"><path d="M14 2 8 7v5h12V7zM2 14h6l4 2h6l6-3v3l-7 4H9l-7-2z"/></svg>Mortgage</div>
  </div>

  <div class="abs price-tag"><small>Single Family Home</small><strong>$380,000</strong></div>

  <div class="abs thumbs">
    <div class="thumb"><div role="img" aria-label="White living room" style="background:linear-gradient(#e8e8ea,#c8c8cc)"></div></div>
    <div class="thumb"><div role="img" aria-label="Green room with armchair" style="background:linear-gradient(#a6d24a,#7fb22c)"></div></div>
    <div class="thumb"><div role="img" aria-label="Bright bedroom" style="background:linear-gradient(#f2ede6,#c9a679)"></div></div>
    <div class="thumb"><div role="img" aria-label="Orange room with chair" style="background:linear-gradient(#f0924a,#d9692a)"></div></div>
    <div class="thumb"><div role="img" aria-label="Light study room" style="background:linear-gradient(#eef0ea,#9cc06a)"></div></div>
    <div class="thumb"><div role="img" aria-label="Warm lounge interior" style="background:linear-gradient(#c4602e,#f0d0b4)"></div></div>
    <div class="thumb"><div role="img" aria-label="Red wall with green sofa" style="background:linear-gradient(#d8362a,#9fcc2a)"></div></div>
    <div class="thumb"><div role="img" aria-label="Open kitchen" style="background:linear-gradient(#d8d2cc,#8a7a70)"></div></div>
    <div class="thumb"><div role="img" aria-label="Yellow room with chair" style="background:linear-gradient(#f5d24a,#e9b52a)"></div></div>
    <div class="thumb"><div role="img" aria-label="Modern living room" style="background:linear-gradient(#d8d0c6,#6c5a4c)"></div></div>
    <div class="thumb"><div role="img" aria-label="Green room with red chairs" style="background:linear-gradient(#a8cf5a,#d8453a)"></div></div>
    <div class="thumb active"><div role="img" aria-label="House exterior" style="background:linear-gradient(#3c70c4,#e2d8d2 60%,#4a5a35)"></div></div>
  </div>
</section>

<div class="abs description">
  <p>Lorem ipsum dolor sit amet, consectetuer adipiscing elit, sed diam nonummy nibh euismod tincidunt ut laoreet dolore magna aliquam erat volutpat. Ut wisi enim ad minim veniam, quis nostrud exerci tation ullamcorper suscipit lobortis nisl ut aliquip ex ea commodo consequat. Duis autem vel eum iriure dolor in hendrerit in vulputate velit esse molestie consequat, vel illum dolore eu feugiat nulla facilisis at vero eros et accumsan et iusto odio dignissim qui blandit praesent luptatum zzril delenit augue duis dolore te feugait nulla facilisi.</p>
  <p>Nam liber tempor cum soluta nobis eleifend option congue nihil imperdiet doming id quod mazim placerat facer possim assum. Typi non habent claritatem insitam; est usus legentis in iis qui facit eorum claritatem. Investigationes</p>
</div>

<aside class="card search-widget">
  <div class="widget-head"><svg viewBox="0 0 14 14"><circle cx="6" cy="6" r="4.2" fill="none" stroke="#fff" stroke-width="2"/><path d="M9 9l4 4" stroke="#fff" stroke-width="2.4"/></svg>Search Widget</div>
  <span class="field" style="top:67px">Type</span><div class="select" style="top:57px">Any<b></b></div>
  <span class="field" style="top:101px">Beds</span><div class="select" style="top:91px">Any<b></b></div>
  <span class="field" style="top:134px">Baths</span><div class="select" style="top:124px">Any<b></b></div>
  <span class="field" style="top:168px">City</span><div class="select" style="top:158px">Any<b></b></div>
  <span class="field" style="top:201px">Status</span><div class="select" style="top:191px">Any<b></b></div>
  <div class="range" style="top:230px">Price Range <strong>100000 - 500000</strong></div>
  <div class="slider" style="top:251px"><i style="left:12px"></i><i style="left:90px"></i></div>
  <div class="widget-btn">Search</div>
</aside>

<aside class="card featured">
  <h2>Featured Property</h2>
  <div class="abs featured-photo" role="img" aria-label="Photo of the featured family house"></div>
  <div class="abs ribbon"><small>Single Family Home</small><strong>$380,000</strong></div>
  <h3>1820 Palm Crest Dr, Coral Fl 33150</h3>
  <p>Lorem ipsum dolor sit amet, consectetuer adipiscing elit, sed diam nonummy nibh…</p>
</aside>

<h2 class="recent">Recent Posts</h2>
<div class="recent-item">Web Based Tool Helps Commercial Real Estate</div>

</body>
</html>
```